Tallowreed Advisory Partners Business Card Design

We have the logo we just need someone to design a modern business card design.

Name: Desmond Munkalt
Phone: 3055550148
Mobile: 9175550193
Web:www.tallowreedadvisory.example
email: dmunkalt@tallowreedadvisory.example
Company: Tallowreed Advisory Partners
Title: CEO

Address: 718 Quillmore Ave, Miami, Florida 33190

Target Market(s)

companies over 100 employees

Industry/Entity Type

Business

```html
<!DOCTYPE html>
<html lang="en">
<head>
<meta charset="utf-8">
<title>Tallowreed Advisory Partners – Business Card</title>
<link href="https://fonts.googleapis.com/css2?family=Lato:wght@400;700;900&display=swap" rel="stylesheet">
<style>
  :root {
    --backdrop: #2a2a2a;
    --card-white: #ffffff;
    --card-grey: #e4e5e8;
    --brand-blue: #1d5ee6;
    --brand-navy: #0b1330;
    --ink: #1b1b1b;
    --faint-mark: #dfe5f1;
  }
  * { margin: 0; padding: 0; box-sizing: border-box; }
  html, body {
    width: 1200px; height: 900px; overflow: hidden;
    background: var(--backdrop);
    font-family: "Lato", Arial, sans-serif;
  }
  .stage { position: relative; width: 1200px; height: 900px; }

  .card {
    position: absolute;
    width: 560px; height: 320px;
    overflow: hidden;
    box-shadow: 0 18px 40px rgba(0,0,0,.55);
  }

  /* Back of card */
  .card-back {
    left: 70px; top: 90px;
    background: linear-gradient(120deg, var(--card-grey) 0%, var(--card-white) 55%, var(--card-grey) 100%);
  }
  .card-back .faint-circle {
    position: absolute; left: 170px; top: 20px;
    width: 280px; height: 280px; border-radius: 50%;
    background: var(--faint-mark); opacity: .75;
  }
  .card-back .company {
    position: absolute; left: 0; right: 0; top: 126px;
    text-align: center;
    color: var(--brand-blue); font-size: 27px; font-weight: 400;
  }
  .card-back .tagline {
    position: absolute; left: 0; right: 0; top: 166px;
    text-align: center;
    color: var(--ink); font-size: 15px; letter-spacing: .3px;
  }

  /* Front of card */
  .card-front {
    left: 570px; top: 480px;
    background: linear-gradient(160deg, var(--card-white) 40%, var(--card-grey) 100%);
  }
  .card-front .swoosh { position: absolute; inset: 0; }
  .brand {
    position: absolute; right: 34px; top: 30px;
    display: flex; align-items: center; gap: 10px;
  }
  .brand-dot { width: 34px; height: 34px; border-radius: 50%; background: var(--brand-blue); }
  .brand-name { font-size: 26px; font-weight: 900; color: var(--ink); letter-spacing: .5px; }

  .person { position: absolute; left: 42px; top: 106px; }
  .person-name { color: var(--brand-blue); font-size: 19px; line-height: 23px; }
  .person-title { color: var(--brand-blue); font-size: 14px; line-height: 17px; margin-left: 6px; }
  .address { color: var(--ink); font-size: 13.5px; line-height: 17px; margin-top: 10px; }

  .contacts { list-style: none; margin-top: 10px; }
  .contacts li {
    display: flex; align-items: center; gap: 12px;
    color: var(--ink); font-size: 14.5px; line-height: 22px;
  }
  .contacts svg { width: 14px; height: 14px; fill: var(--brand-navy); flex: none; }

  .website {
    position: absolute; right: 24px; bottom: 18px;
    color: var(--card-white); font-size: 13px; line-height: 16px; letter-spacing: .3px;
  }
</style>
</head>
<body>
<main class="stage">

  <section class="card card-back" aria-label="Card back">
    <div class="faint-circle"></div>
    <h1 class="company">Tallowreed Advisory Partners</h1>
    <p class="tagline">companies over 100 employees</p>
  </section>

  <section class="card card-front" aria-label="Card front">
    <svg class="swoosh" viewBox="0 0 560 320" preserveAspectRatio="none" aria-hidden="true">
      <path d="M0,276 C140,312 300,300 400,236 C460,196 520,180 560,176 L560,320 L0,320 Z" fill="var(--brand-navy)"/>
      <path d="M0,283 C140,318 306,306 406,243 C464,204 522,188 560,184 L560,320 L0,320 Z" fill="var(--card-white)"/>
      <path d="M0,289 C140,322 312,312 412,250 C468,212 524,196 560,192 L560,320 L0,320 Z" fill="var(--brand-blue)"/>
    </svg>

    <div class="brand">
      <span class="brand-dot"></span>
      <span class="brand-name">TALLOWREED</span>
    </div>

    <div class="person">
      <p class="person-name">Desmond Munkalt</p>
      <p class="person-title">CEO</p>
      <p class="address">718 Quillmore Ave, Miami, Florida 33190</p>
      <ul class="contacts">
        <li>
          <svg viewBox="0 0 24 24"><path d="M6.6 10.8a15.1 15.1 0 0 0 6.6 6.6l2.2-2.2a1 1 0 0 1 1-.25 11.4 11.4 0 0 0 3.6.57 1 1 0 0 1 1 1V20a1 1 0 0 1-1 1A17 17 0 0 1 3 4a1 1 0 0 1 1-1h3.5a1 1 0 0 1 1 1c0 1.25.2 2.45.57 3.6a1 1 0 0 1-.25 1z"/></svg>
          3055550148
        </li>
        <li>
          <svg viewBox="0 0 24 24"><path d="M7 1h10a2 2 0 0 1 2 2v18a2 2 0 0 1-2 2H7a2 2 0 0 1-2-2V3a2 2 0 0 1 2-2zm0 3v14h10V4zm5 15.5a1 1 0 1 0 0 2 1 1 0 0 0 0-2z"/></svg>
          9175550193
        </li>
        <li>
          <svg viewBox="0 0 24 24"><path d="M2 5h20v14H2zm2 2v.5l8 5 8-5V7zm0 2.9V17h16V9.9l-8 5z"/></svg>
          dmunkalt@tallowreedadvisory.example
        </li>
      </ul>
    </div>

    <p class="website">www.tallowreedadvisory.example</p>
  </section>

</main>
</body>
</html>
```